Ridgeline Stick Works
Custom Wood Bats
guaranteed please...
For some reason, my numbers aren't showing up, but for the ones I rated, could you put the rest of the stationary with the cards? Looks great you all. Thanks!
increase the price please.....
#3, I like that. Can you make the seams red on the front of the ball or will the address not show up if you do?
Can you combine 7 & 8
Hi - so it is ok to alter the logo colors on the logo itself?
I would like to see some different colors. Maybe a navy blue print on the logo and then in the red part. Leave the ball white with red stitches. Look forward to seeing your interpretations.
Just uploaded it. My name doesn't have a "c" in it. Could you also put "Ridgeline Stick Works" somewhere on the front of the card? Also, I'm not a big fan of the all caps. Thanks for your design.
can you upload the original logo,please?

```html
<!DOCTYPE html>
<html lang="en">
<head>
<meta charset="utf-8">
<title>Ridgeline Stick Works – Business Card</title>
<link href="https://fonts.googleapis.com/css2?family=Fira+Sans:ital,wght@0,400;0,500;0,600;1,400;1,500&display=swap" rel="stylesheet">
<style>
  :root {
    --navy: #223d85;
    --white: #ffffff;
    --stage: #ececec;
    --label: #444444;
  }
  * { margin: 0; padding: 0; box-sizing: border-box; }
  html, body { width: 1200px; height: 924px; overflow: hidden; }
  body {
    background: var(--stage);
    font-family: "Fira Sans", Arial, sans-serif;
    position: relative;
  }
  .card {
    position: absolute;
    left: 200px;
    width: 665px;
    height: 392px;
    overflow: hidden;
    box-shadow: 4px 6px 10px rgba(0,0,0,0.35);
  }
  .card--front { top: 38px; background: var(--white); }
  .card--back { top: 470px; background: var(--navy); }

  .side-label {
    position: absolute;
    left: 992px;
    font-size: 22px;
    color: var(--label);
  }
  .side-label--front { top: 228px; }
  .side-label--back { top: 643px; }

  /* front */
  .brand-name {
    position: absolute;
    left: 40px; top: 72px;
    width: 300px;
    font-size: 38px;
    line-height: 1.05;
    font-weight: 600;
    color: var(--navy);
  }
  .mailing-address {
    position: absolute;
    left: 92px; top: 184px;
    font-size: 17px;
    line-height: 26px;
    color: var(--navy);
    font-style: normal;
  }
  .contact-top {
    position: absolute;
    right: 40px; top: 48px;
    text-align: right;
    font-size: 18px;
    line-height: 26px;
    font-weight: 500;
    color: var(--navy);
  }
  .name-band {
    position: absolute;
    left: 0; top: 272px;
    width: 100%; height: 78px;
    background: var(--navy);
  }
  .holder-name {
    position: absolute;
    left: 42px; top: 280px;
    font-size: 32px;
    font-weight: 500;
    color: var(--white);
  }
  .holder-email {
    position: absolute;
    left: 42px; top: 322px;
    font-size: 18px;
    color: var(--white);
  }
  .bats-art {
    position: absolute;
    border-radius: 6px;
  }
  .card--front .bats-art {
    left: 400px; top: 125px; width: 250px; height: 250px;
    background: linear-gradient(180deg, rgba(34,61,133,0.16), rgba(34,61,133,0.30));
  }
  .card--back .bats-art {
    left: 400px; top: 130px; width: 250px; height: 238px;
    background: linear-gradient(180deg, rgba(255,255,255,0.22), rgba(255,255,255,0.38));
  }
  .role-title {
    position: absolute;
    left: 475px; top: 242px; width: 100px;
    text-align: center;
    font-size: 21px;
    font-style: italic;
    color: var(--navy);
  }

  /* back */
  .back-url {
    position: absolute;
    left: 42px; top: 42px;
    font-size: 20px;
    font-weight: 500;
    color: var(--white);
  }
  .slogan-band {
    position: absolute;
    left: 0; top: 242px;
    width: 100%; height: 100px;
    background: var(--white);
  }
  .slogan {
    position: absolute;
    left: 42px; top: 277px;
    font-size: 38px;
    font-style: italic;
    font-weight: 500;
    color: var(--navy);
  }
</style>
</head>
<body>

  <section class="card card--front" aria-label="Card front">
    <div class="brand-name">Ridgeline<br>Stick Works</div>
    <address class="mailing-address">P.O. Box 412<br>Millbrook, NC 28000</address>
    <div class="contact-top">555.014.2290<br>www.ridgelinesticks.com</div>

    <div class="name-band"></div>
    <div class="holder-name">Dale Harmon</div>
    <div class="holder-email">dale@ridgelinesticks.com</div>

    <div class="bats-art" role="img" aria-label="Two crossed baseball bats behind a home plate"></div>
    <div class="role-title">Owner</div>
  </section>

  <section class="card card--back" aria-label="Card back">
    <div class="back-url">www.ridgelinesticks.com</div>
    <div class="slogan-band"></div>
    <div class="slogan">Custom Wood Bats</div>

    <div class="bats-art" role="img" aria-label="Two crossed white baseball bats behind a home plate"></div>
  </section>

  <div class="side-label side-label--front">front</div>
  <div class="side-label side-label--back">back</div>

</body>
</html>
```